Purrline Fest Ticket Card Design

We’re looking to create a complimentary “ticket” card for Purrline Fest that can be handed out physically. We host an event for cat lovers. The card should feel special and collectible. Size will be a standard business card (3.5" x 2") Orientation is open to designer recommendation. This ticket will be used as a complimentary entry pass for select guests, partners, & giveaways. Key elements to Include are the Purrline Fest logo (provided), the words “Complimentary Ticket” or similar wording (open to creative phrasing and cat puns) A blank space for the Event date (to be written in) & Ticket number (to be written in) . Event Name is always "Purrline Bazaar & Rescue Gala". We want the ticket to feel clean & modern but slightly playful with a cat-inspired touch (think clever, not kitschy). Could include a subtle cat motif or texture (e.g., whisker lines, paw detail, soft patterning) Open to unique layout ideas that still leave clear writing space. Avoid overcrowding of elements. Ticket should also have fine print "This ticket is not redeemable for cash and cannot be combined with any other offers or discounts, can only be used for the date indicated"

Target Market(s)

Women

Industry/Entity Type

pets

Colors
6B429C
8869AF
B7A5CE
E3DAEB
F3F0F8

Requirements
Must have
• Purrline Fest Logo & words around complimentary ticket as well as the fine print
Nice to have
• cat-inspired touch (think clever, not kitschy). Could include a subtle cat motif or texture (e.g., whisker lines, paw detail, soft patterning)
Should not have
• should not look cartoony

```html
<!DOCTYPE html>
<html lang="en">
<head>
<meta charset="utf-8">
<title>Purrline Fest – Complimentary Ticket</title>
<link rel="stylesheet" href="https://fonts.googleapis.com/css2?family=Montserrat:wght@700;800;900&family=Poppins:wght@400;500;600&display=swap">
<style>
  :root {
    --backdrop: #1a0e30;
    --purple: #6b429c;
    --purple-mid: #8869af;
    --lavender: #b7a5ce;
    --lilac: #e3daeb;
    --mist: #f3f0f8;
    --white: #ffffff;
    --ink: #111111;
    --rule: #555555;
  }
  * { margin: 0; padding: 0; box-sizing: border-box; }
  html, body { width: 750px; height: 1200px; overflow: hidden; }
  body { background: var(--backdrop); position: relative; font-family: "Poppins", sans-serif; }

  .ticket-card {
    position: absolute; left: 112px; top: 141px;
    width: 526px; height: 918px;
    background: var(--white); overflow: hidden;
  }
  .hero-art {
    position: absolute; left: 0; top: 0; width: 526px; height: 390px;
    background:
      radial-gradient(ellipse 230px 200px at 300px 370px, var(--white) 0%, var(--mist) 35%, rgba(243,240,248,0) 75%),
      linear-gradient(180deg, var(--purple) 0%, var(--purple) 38%, var(--purple-mid) 62%, var(--lavender) 80%, var(--lilac) 92%, var(--white) 100%);
  }
  .hero-title { position: absolute; left: 0; top: 0; width: 526px; height: 260px; }
  .hero-title text { font-family: "Montserrat", sans-serif; font-weight: 900; fill: var(--white); }

  .brand-name {
    position: absolute; left: 0; top: 392px; width: 526px;
    text-align: center; font-family: "Montserrat", sans-serif; font-weight: 900;
    font-size: 54px; line-height: 54px; color: var(--ink); letter-spacing: -1px;
  }

  .event-date {
    position: absolute; left: 104px; top: 544px; width: 76px;
    font-family: "Montserrat", sans-serif; font-weight: 900; text-align: center;
  }
  .event-date .weekday { color: var(--purple); font-size: 16px; line-height: 18px; letter-spacing: -0.5px; }
  .event-date .month { color: var(--ink); font-size: 26px; line-height: 26px; letter-spacing: -1px; }
  .event-date .day { color: var(--ink); font-size: 66px; line-height: 58px; letter-spacing: -3px; }
  .event-date .year {
    display: block; margin-top: 4px; background: var(--purple); color: var(--white);
    font-size: 20px; line-height: 30px; letter-spacing: 0;
  }
  .date-divider {
    position: absolute; left: 212px; top: 547px; width: 2px; height: 136px;
    background: var(--purple);
  }

  .event-name {
    position: absolute; left: 236px; top: 543px; width: 280px;
    font-family: "Montserrat", sans-serif; font-weight: 900;
    font-size: 31px; line-height: 37px; letter-spacing: -1.2px;
    color: var(--purple); text-transform: uppercase;
  }
  .event-name .lead { color: var(--ink); }

  .section-rule {
    position: absolute; left: 49px; top: 705px; width: 428px; height: 1px; background: var(--rule);
  }
  .fine-print {
    position: absolute; left: 33px; top: 720px; width: 460px;
    text-align: center; font-size: 15.5px; line-height: 20px; color: var(--ink);
    letter-spacing: 0.1px; white-space: nowrap;
  }
  .admits {
    position: absolute; left: 0; top: 795px; width: 526px; text-align: center;
    font-family: "Montserrat", sans-serif; font-weight: 800; font-size: 18px; color: var(--ink);
  }
  .admits .accent { color: var(--purple); }

  .ticket-number {
    position: absolute; left: 70px; top: 834px; width: 386px; height: 34px;
    border: 1px solid var(--purple-mid); border-radius: 17px; overflow: hidden; display: flex;
  }
  .ticket-number .label {
    width: 148px; height: 100%; background: var(--purple); color: var(--white);
    border-radius: 0 17px 17px 0;
    font-family: "Montserrat", sans-serif; font-weight: 800; font-size: 17px;
    letter-spacing: 1.5px; line-height: 33px; padding-left: 20px;
  }
  .ticket-number .write-in { flex: 1; }
</style>
</head>
<body>
  <main class="ticket-card">
    <div class="hero-art" role="img" aria-label="White cat silhouette seen from behind with a long curling tail, on purple"></div>
    <svg class="hero-title" viewBox="0 0 526 260" aria-label="Complimentary Ticket">
      <path id="arc-small" d="M 233 93 Q 390 62 495 148" fill="none"/>
      <path id="arc-large" d="M 228 148 Q 380 120 478 218" fill="none"/>
      <text font-size="27"><textPath href="#arc-small">COMPLIMENTARY</textPath></text>
      <text font-size="54"><textPath href="#arc-large">TICKET</textPath></text>
    </svg>

    <h1 class="brand-name">Purrline<br>Fest</h1>

    <div class="event-date">
      <div class="weekday">SUNDAY</div>
      <div class="month">SEPT</div>
      <div class="day">27</div>
      <span class="year">2026</span>
    </div>
    <div class="date-divider"></div>

    <h2 class="event-name">
      <span class="lead">Purrline</span><br>Bazaar &amp;<br>Rescue<br>Gala
    </h2>

    <div class="section-rule"></div>
    <p class="fine-print">This ticket is not redeemable for cash and cannot<br>be combined with any other offers or discounts,<br>can only be used for the date indicated.</p>
    <p class="admits"><span class="accent">ADMITS</span> 1 PERSON</p>

    <div class="ticket-number">
      <span class="label">Ticket No</span>
      <span class="write-in"></span>
    </div>
  </main>
</body>
</html>
```